Website for an electrical contractor :)

We are after a web site which can show pictures of our jobs and our capability in a professional, creative and easily understood way.

----- Brightmoor Electrical ------

We really want a visually good looking website with three sections

Section one:
'Completed projects'
We have a few pictures of jobs which we've completed and would like to show off with a brief description. (see uploads)

Section two:
'Our capabilities'
Just a list of what services we offer

Section three:
We would like a 'contact us' section which people can send us a short msg and upload a file for plans to be able to send to us. We would need their name, phone number and email details. We would also need a short privacy policy saying 'we do not disclose information to third parties'.
We also want to display our contact number and postal address

Good luck :)

Target Market(s)

Adults 25 years+
Business owners
Builders
Real estate agents

Industry/Entity Type

Electrical

Colors

Designer to choose colors to be used in the design.

Requirements
Must have
• Visually appealing
Easy to understand
In the 'Completed projects' section, must have a list for each project we do i can upload pictures for it.

```html
<!DOCTYPE html>
<html lang="en">
<head>
<meta charset="utf-8">
<title>Brightmoor Electrical</title>
<link href="https://fonts.googleapis.com/css2?family=Raleway:wght@400;500;600;700&family=Open+Sans:wght@400;600&display=swap" rel="stylesheet">
<style>
:root{
  --red:#e3101e;
  --red-deep:#b80c16;
  --ink:#222;
  --muted:#555;
  --dark:#1b1b1b;
  --darker:#111;
  --field:#2c2c2c;
  --white:#fff;
}
*{margin:0;padding:0;box-sizing:border-box}
html,body{width:718px;height:1200px;overflow:hidden;background:var(--white)}
body{position:relative;font-family:"Open Sans",sans-serif;color:var(--ink)}
.abs{position:absolute}

/* header */
.site-header{position:absolute;left:0;top:0;width:718px;height:56px;background:var(--white)}
.brand{position:absolute;left:107px;top:16px;display:flex;align-items:center;gap:7px}
.brand-dot{width:12px;height:12px;border-radius:50%;background:var(--red)}
.brand-name{font-family:"Raleway",sans-serif;font-weight:500;font-size:17px;color:#333;letter-spacing:-.2px}
.main-nav{position:absolute;top:23px;left:0;font-family:"Raleway",sans-serif;font-weight:600;font-size:8.5px}
.main-nav a{position:absolute;white-space:nowrap;color:#222;text-decoration:none}
.main-nav a.active{color:var(--red)}

/* hero */
.hero{position:absolute;left:0;top:56px;width:718px;height:331px;
  background:linear-gradient(180deg,#3f7fcf 0%,#7aa8dc 30%,#9a9a92 55%,#8a867c 75%,#a9a59b 100%)}
.hero-card{position:absolute;left:183px;top:106px;width:351px;height:104px;background:rgba(20,20,20,.82);text-align:center;padding-top:19px}
.hero-kicker{font-family:"Raleway",sans-serif;font-weight:600;font-size:13px;color:var(--red);letter-spacing:.2px}
.hero-title{font-family:"Raleway",sans-serif;font-weight:700;font-size:21px;color:var(--white);margin-top:1px}
.hero-text{font-size:7px;line-height:9.5px;color:#ddd;margin:4px auto 0;width:300px}
.hero-arrow{position:absolute;top:140px}

/* projects */
.section-title{position:absolute;left:0;width:718px;text-align:center;font-family:"Raleway",sans-serif;font-weight:400;font-size:17px;color:#333}
.project{position:absolute;top:446px;width:158px}
.project-photo{height:83px}
.project-title{font-family:"Raleway",sans-serif;font-weight:500;font-size:9.5px;color:var(--red);margin-top:8px}
.project-text{font-size:5.6px;line-height:9.5px;color:var(--muted);margin-top:3px}

/* capabilities */
.capabilities{position:absolute;left:0;top:629px;width:718px;height:283px;
  background:linear-gradient(180deg,#e8101c 0%,#dc0f1a 50%,#e41420 100%)}
.cap-tab{position:absolute;left:266px;top:0}
.cap-title{position:absolute;top:11px;left:0;width:718px;text-align:center;font-family:"Raleway",sans-serif;font-size:15.5px;color:var(--white)}
.cap-group{position:absolute;top:57px;font-family:"Raleway",sans-serif;font-size:11px;color:#7a0a10}
.cap-list{position:absolute;top:81px;list-style:none;font-size:6.5px;color:var(--white);line-height:13.8px}
.cap-list li{position:relative;padding-left:9px;white-space:nowrap}
.cap-list li::before{content:"";position:absolute;left:0;top:6px;border-left:3px solid #fff;border-top:2.5px solid transparent;border-bottom:2.5px solid transparent}

/* contact */
.contact{position:absolute;left:0;top:912px;width:718px;height:253px;background:var(--dark)}
.contact-title{position:absolute;top:37px;left:0;width:718px;text-align:center;font-family:"Raleway",sans-serif;font-weight:500;font-size:16px;color:var(--white)}
.field{position:absolute;background:var(--field);border:1px solid #333;font-size:6.2px;color:#aaa;padding:6px 8px}
.submit{position:absolute;left:114px;top:202px;width:63px;height:20px;background:var(--red);color:var(--white);font-family:"Raleway",sans-serif;font-weight:700;font-size:8.5px;text-align:center;line-height:20px}
.info-label{position:absolute;left:394px;font-size:6.5px;color:#999}
.info-line{position:absolute;left:394px;font-size:7.5px;color:var(--white)}
.social{position:absolute;top:156px;width:13px;height:13px;background:var(--white);border-radius:2px}

/* footer */
.site-footer{position:absolute;left:0;top:1165px;width:718px;height:35px;background:var(--darker)}
.footer-note{position:absolute;left:113px;top:14px;font-size:5.5px;color:#888}
</style>
</head>
<body>

<header class="site-header">
  <div class="brand"><span class="brand-dot"></span><span class="brand-name">Brightmoor Electrical</span></div>
  <nav class="main-nav">
    <a class="active" style="left:359px">HOME</a>
    <a style="left:416px">PROJECTS</a>
    <a style="left:489px">SERVICES</a>
    <a style="left:559px">CONTACT</a>
  </nav>
</header>

<section class="hero" role="img" aria-label="Photo of a finished residential house with paved driveway under a blue sky">
  <svg class="hero-arrow" style="left:72px" width="18" height="36" viewBox="0 0 18 36"><polyline points="16,2 2,18 16,34" fill="none" stroke="#fff" stroke-width="2"/></svg>
  <svg class="hero-arrow" style="left:620px" width="18" height="36" viewBox="0 0 18 36"><polyline points="2,2 16,18 2,34" fill="none" stroke="#fff" stroke-width="2"/></svg>
  <div class="hero-card">
    <div class="hero-kicker">CURABITUR VEL MI SIT AMET MAGNA</div>
    <div class="hero-title">MORBI DIAM MAURIS VIVER</div>
    <p class="hero-text">Arbi diam mauris viverra in gravida eu mattis in ante Morbi eget arcu Morbi porta libero id ullamcorper nonummy nibh ligula pulvinar metus eget consectetuer augue</p>
  </div>
</section>

<h2 class="section-title" style="top:410px">Completed Projects</h2>

<article class="project" style="left:107px">
  <div class="project-photo" role="img" aria-label="Photo of an office interior with ceiling lighting" style="background:linear-gradient(180deg,#6b6560,#3a3632 60%,#9a938a)"></div>
  <h3 class="project-title">Project Tittle here</h3>
  <p class="project-text">Vivamus porttitor purus nisi eleifend libero a tempus libero lectus feugiat felis Morbi diam mauris viverra in gravida eu mattis in ante Morbi eget arcu Morbi porta libero id ullamcorper nonummy nibh ligula pulvinar</p>
</article>
<article class="project" style="left:280px">
  <div class="project-photo" role="img" aria-label="Photo of a concrete commercial building" style="background:linear-gradient(180deg,#2f5fae,#6f8fc0 30%,#c9c6bf 55%,#a8a59e)"></div>
  <h3 class="project-title">Project Tittle here</h3>
  <p class="project-text">Vivamus porttitor purus nisi eleifend libero a tempus libero lectus feugiat felis Morbi diam mauris viverra in gravida eu mattis in ante Morbi eget arcu Morbi porta libero id ullamcorper nonummy nibh ligula</p>
</article>
<article class="project" style="left:453px">
  <div class="project-photo" role="img" aria-label="Photo of a new industrial warehouse unit" style="background:linear-gradient(180deg,#7fa3d2,#b5c6dc 35%,#777 55%,#9a9894)"></div>
  <h3 class="project-title">Project Tittle here</h3>
  <p class="project-text">Vivamus porttitor purus nisi eleifend libero a tempus libero lectus feugiat felis Morbi diam mauris viverra in gravida eu mattis in ante Morbi eget arcu Morbi porta libero id ullamcorper nonummy nibh ligula pulvinar</p>
</article>

<section class="capabilities" role="img" aria-label="Red-tinted photo of a finished interior behind the capabilities list">
  <svg class="cap-tab" width="186" height="36" viewBox="0 0 186 36"><polygon points="0,0 186,0 170,36 16,36" fill="#c80d18"/></svg>
  <h2 class="cap-title">Our Capabilities</h2>
  <div class="cap-group" style="left:107px">Residential</div>
  <div class="cap-group" style="left:373px">Commercial / Industrial</div>
  <ul class="cap-list" style="left:107px">
    <li>24hr Support / faults</li><li>RCD (Safety Switch) installations</li><li>Smoke alarms</li><li>Power points</li><li>Lighting points</li><li>External lighting</li><li>Sensor lighting</li><li>Switching</li><li>Antennas and Arial points</li><li>Dimmers</li><li>Ceiling fans</li>
  </ul>
  <ul class="cap-list" style="left:221px">
    <li>Exhaust fans</li><li>Kitchen / Bathroom Projects</li><li>Re-wires</li><li>Smart wiring</li><li>Phone points</li><li>Data points</li><li>Mains/sub mains cabling</li><li>Switchboard installations/relocations</li><li>Compliance investigations/inspections</li><li>Concrete and wall chasing</li><li>Temporary builders site power</li>
  </ul>
  <ul class="cap-list" style="left:371px">
    <li>24hr Support / faults</li><li>Lighting/power design and</li><li style="padding-left:9px">consultation</li><li>Commercial lighting</li><li>Emergency and exit lighting</li><li>Led strip lighting</li><li>Energy efficient lighting</li><li>Temporary lighting</li><li>Illuminated signage</li><li>Switchboard relocations</li><li>Maintenance</li>
  </ul>
  <ul class="cap-list" style="left:493px">
    <li>RCD installation</li><li>Phone/data points</li><li>Data cabinets</li><li>Data Networking</li><li>IDF installations/relocations</li><li>All power requirements</li><li>All three phase power requirements</li><li>Electrical rip outs / Disconnections</li><li>Thermal Imaging scans</li><li>Concrete and wall chasing</li>
  </ul>
</section>

<section class="contact">
  <h2 class="contact-title">CONTACT US</h2>
  <div class="field" style="left:113px;top:81px;width:231px;height:19px">Your Name</div>
  <div class="field" style="left:113px;top:104px;width:114px;height:20px">Email address</div>
  <div class="field" style="left:231px;top:104px;width:113px;height:20px">Phone</div>
  <div class="field" style="left:113px;top:128px;width:114px;height:20px">Submit Resume</div>
  <div class="field" style="left:231px;top:128px;width:113px;height:20px">Privacy Saying</div>
  <div class="field" style="left:113px;top:152px;width:231px;height:46px">Your Messege</div>
  <div class="submit">SUBMIT</div>

  <div class="info-label" style="top:83px">Contact Information</div>
  <div class="info-line" style="top:95px">48 Larkspur Avenue #B</div>
  <div class="info-line" style="top:108px">Texas 75012 TX</div>
  <svg class="abs" style="left:394px;top:124px" width="10" height="10" viewBox="0 0 24 24"><path fill="#fff" d="M6.6 10.8a15.1 15.1 0 0 0 6.6 6.6l2.2-2.2c.3-.3.7-.4 1-.2 1.1.4 2.3.6 3.6.6.6 0 1 .4 1 1V20c0 .6-.4 1-1 1A17 17 0 0 1 3 4c0-.6.4-1 1-1h3.5c.6 0 1 .4 1 1 0 1.2.2 2.4.6 3.6.1.3 0 .7-.2 1z"/></svg>
  <div class="info-line" style="left:407px;top:124px">555.204.7781</div>
  <svg class="abs" style="left:460px;top:125px" width="12" height="9" viewBox="0 0 12 9"><rect x="0" y="0" width="12" height="9" fill="#fff"/><polyline points="0,0 6,5 12,0" fill="none" stroke="#1b1b1b" stroke-width="1"/></svg>
  <div class="info-line" style="left:474px;top:124px">hello@brightmoorelectrical.com</div>
  <div class="info-label" style="left:396px;top:147px">Get in touch with us</div>
  <span class="social" style="left:397px"></span>
  <span class="social" style="left:413px"></span>
  <span class="social" style="left:429px"></span>
</section>

<footer class="site-footer">
  <p class="footer-note">© 2015 COMPANY NAME &nbsp;ALL RIGHT RESERVED &nbsp;TERM OF USE</p>
</footer>

</body>
</html>
```